Naturopath Practitioner Card Design

I am a naturopath needing a design for a business card mainly to show that I am a naturopath and have some contact details to give to prospective clients. I am open minded about the design and what is on the second side of the card whether it just be some artwork or space for details, appointment times etc. Naturopathy is the practice of natural medicine that uses a holistic approach and incorporates herbal and nutritional medicine.

Industry/Entity Type

Business

Contact Information for Business Card

Tom Welby NaturopathBHSc (Naturopathy) Member PHRA 0492 815 306 tom.welby@mailbright.com www.tomwelbynaturopathy.com.au

Requirements
Nice to have
• Would prefer some kind of original pattern/art work/logo rather than an image, not fussed if its very simple/basic
• I am open to any colour but think I would prefer a more earthy sandy clay etc type style than the greens that are commonly associated with naturopathy.
Should not have
• Don't really want to have generic stock images on it

```html
<!DOCTYPE html>
<html lang="en">
<head>
<meta charset="utf-8">
<title>Tom Welby Naturopath – Business Card</title>
<link rel="stylesheet" href="https://fonts.googleapis.com/css2?family=Arvo:wght@400;700&family=Roboto:wght@400&display=swap">
<style>
  :root {
    --page-bg: #ece9e4;
    --leaf-deep: #5f9a1c;
    --leaf-bright: #a6cf3a;
    --leaf-pale: #e6eed3;
    --leaf-pale-2: #f1f4e3;
    --panel: rgba(244, 247, 236, 0.86);
    --frame: #ffffff;
    --brand-green: #5a8a2a;
    --text-grey: #6a6a68;
    --rule-grey: #707070;
  }
  * { box-sizing: border-box; margin: 0; padding: 0; }
  html, body { width: 1200px; height: 1000px; overflow: hidden; }
  body { background: var(--page-bg); position: relative; font-family: "Roboto", Arial, sans-serif; }

  .card { position: absolute; width: 674px; height: 416px; overflow: hidden; box-shadow: 0 3px 8px rgba(0,0,0,0.18); }
  .card--front { left: 260px; top: 60px; }
  .card--back { left: 262px; top: 512px; }

  .leaf-photo { position: absolute; inset: 0; }
  .leaf-photo--vivid { background: radial-gradient(ellipse at 30% 55%, var(--leaf-bright) 0%, #8fbf2c 45%, var(--leaf-deep) 100%); }
  .leaf-photo--pale { background: linear-gradient(160deg, var(--leaf-pale-2) 0%, var(--leaf-pale) 60%, #dfe8c8 100%); }

  .front-panel { position: absolute; left: 50px; top: 50px; width: 574px; height: 318px; background: var(--panel); }
  .front-frame { position: absolute; left: 57px; top: 57px; width: 560px; height: 304px; border: 2px solid var(--frame); }

  .name { position: absolute; left: 0; right: 0; top: 128px; text-align: center; font-family: "Arvo", Georgia, serif; font-weight: 700; font-size: 50px; color: var(--brand-green); letter-spacing: 1px; }
  .role { position: absolute; left: 0; right: 0; top: 194px; text-align: center; font-family: "Arvo", Georgia, serif; font-size: 24px; color: var(--text-grey); letter-spacing: 6px; }
  .credentials { position: absolute; left: 0; right: 0; top: 252px; text-align: center; font-size: 18px; color: var(--text-grey); }
  .divider { position: absolute; left: 127px; width: 418px; top: 294px; border-top: 2px solid var(--rule-grey); }
  .contact { position: absolute; left: 0; right: 0; top: 313px; text-align: center; font-size: 18px; color: var(--text-grey); }

  .appt-title { position: absolute; left: 0; right: 0; top: 52px; text-align: center; font-family: "Arvo", Georgia, serif; font-weight: 700; font-size: 20px; letter-spacing: 5px; color: var(--brand-green); }
  .appt-label { position: absolute; top: 88px; font-family: "Arvo", Georgia, serif; font-weight: 700; font-size: 15px; color: var(--text-grey); }
  .appt-label--date { left: 56px; }
  .appt-label--time { left: 436px; }
  .appt-table { position: absolute; left: 56px; top: 116px; }
  .cancel-note { position: absolute; left: 0; right: 0; top: 343px; text-align: center; font-family: "Arvo", Georgia, serif; font-weight: 700; font-size: 15px; color: var(--text-grey); }
</style>
</head>
<body>
  <section class="card card--front" aria-label="Business card front">
    <div class="leaf-photo leaf-photo--vivid" role="img" aria-label="Close-up photograph of a backlit green leaf with veins"></div>
    <div class="front-panel"></div>
    <div class="front-frame"></div>
    <h1 class="name">TOM WELBY</h1>
    <p class="role">NATUROPATH</p>
    <p class="credentials">BHSc (Naturopathy) Member PHRA</p>
    <div class="divider"></div>
    <p class="contact">0492 815 306 | tom.welby@mailbright.com</p>
  </section>

  <section class="card card--back" aria-label="Business card back">
    <div class="leaf-photo leaf-photo--pale" role="img" aria-label="Faded photograph of a pale leaf with veins"></div>
    <h2 class="appt-title">YOUR NEXT APPOINTMENT</h2>
    <span class="appt-label appt-label--date">Date</span>
    <span class="appt-label appt-label--time">Time</span>
    <svg class="appt-table" width="562" height="214" viewBox="0 0 562 214" aria-label="Appointment date and time table">
      <g fill="none" stroke="#707070" stroke-width="2">
        <rect x="1" y="1" width="560" height="211"/>
        <line x1="1" y1="54" x2="561" y2="54"/>
        <line x1="1" y1="104" x2="561" y2="104"/>
        <line x1="1" y1="155" x2="561" y2="155"/>
        <line x1="381" y1="1" x2="381" y2="212"/>
      </g>
    </svg>
    <p class="cancel-note">Please give 24 hours notice of cancellation</p>
  </section>
</body>
</html>
```